Heron Accord Business Card

Need a business card for my nonprofit, Heron Accord Inc. Heron Accord is a conflict resolution practice that offers services that help people resolve problems peacefully.

Got Conflict? Try Conflict Coaching. Initial consultation is complimentary

Marisol Daventry-Kuhl, PhD
Heron Accord Inc.
www.heronaccord-example.org
E: info@heronaccord-example.org
P: 555-318-4927

Would like the attached logo on it, as well as our slogan, which is Finding Calm Around the RoomĀ®

```html
<!DOCTYPE html>
<html lang="en">
<head>
<meta charset="utf-8">
<title>Heron Accord Business Card</title>
<link rel="stylesheet" href="https://fonts.googleapis.com/css2?family=Source+Sans+3:wght@400;600;700&display=swap">
<style>
  :root {
    --backdrop: #e6e6e8;
    --card-red: #ec1c24;
    --card-red-light: #f2343b;
    --paper: #f7f7f6;
    --gold: #c49a22;
    --gold-dark: #a67f16;
    --gold-light: #dcb645;
    --ink: #555558;
    --accent: #e3161f;
    --white: #ffffff;
  }
  * { box-sizing: border-box; margin: 0; padding: 0; }
  html, body {
    width: 1200px; height: 840px; overflow: hidden;
    background: var(--backdrop);
    font-family: "Source Sans 3", "Myriad Pro", Arial, sans-serif;
  }
  .sheet {
    width: 1200px; height: 840px;
    display: flex; flex-direction: column;
    align-items: center; justify-content: center; gap: 48px;
  }
  .card {
    position: relative;
    width: 560px; height: 320px;
    overflow: hidden;
    box-shadow: 0 6px 18px rgba(0,0,0,0.18);
  }

  /* Front */
  .card-front {
    background: linear-gradient(135deg, var(--card-red-light), var(--card-red) 60%);
    color: var(--white);
  }
  .front-mark {
    position: absolute; left: 0; right: 0; top: 108px;
    display: flex; align-items: center; justify-content: center; gap: 14px;
  }
  .front-mark .dot {
    width: 22px; height: 22px; border-radius: 50%;
    background: var(--white);
  }
  .front-mark .name {
    font-size: 38px; font-weight: 600; letter-spacing: 1px;
    color: var(--white);
  }
  .slogan {
    position: absolute; left: 0; right: 0; top: 206px;
    text-align: center;
    font-size: 15px; font-weight: 400; font-style: italic;
  }
  .slogan sup { font-size: 8px; }

  /* Back */
  .card-back { background: var(--paper); }
  .back-band {
    position: absolute; left: 0; right: 0; bottom: 0; height: 64px;
    background: linear-gradient(100deg, var(--gold-light), var(--gold) 55%, var(--gold-dark));
  }
  .back-logo {
    position: absolute; left: 170px; right: 40px; top: 40px;
    text-align: center;
    font-size: 40px; font-weight: 600; letter-spacing: 4px;
    color: var(--gold);
  }
  .contact {
    position: absolute; right: 32px; top: 118px;
    text-align: right; color: var(--ink);
    font-size: 13px; line-height: 22px;
  }
  .contact .person {
    color: var(--accent); font-weight: 700; font-size: 15px;
    margin-bottom: 4px;
  }
  .contact .label { color: var(--accent); font-weight: 700; }
</style>
</head>
<body>
  <main class="sheet">
    <section class="card card-front" aria-label="Card front">
      <div class="front-mark">
        <span class="dot"></span>
        <span class="name">Heron Accord</span>
      </div>
      <p class="slogan">Finding Calm Around the Room<sup>®</sup></p>
    </section>

    <section class="card card-back" aria-label="Card back">
      <div class="back-band" role="img" aria-label="Decorative gold and red sweeping band along the lower edge"></div>

      <div class="back-logo">HERON ACCORD</div>

      <div class="contact">
        <p class="person">Marisol Daventry-Kuhl, PhD</p>
        <p>Heron Accord Inc. 214 Willowmere Court Springfield, Oregon 97477</p>
        <p><span class="label">P:</span> 555-318-4927 <span class="label">E:</span> info@heronaccord-example.org <span class="label">W:</span> www.heronaccord-example.org</p>
      </div>
    </section>
  </main>
</body>
</html>
```